Essential Oils and Chemical Free Skincare Packaging

We have a range of 100% organic 10ml essential oils and 10ml essential oil synergy blends and 50ml spritzer bottles plus chemical free skincare products including two serums, one cleanser, two moisturisers, a lip balm, an eye and lip cream and a body lotion that need new labels, boxes for the products with a fresh new look. Some of these products are in packs or gift packs as seen on the website. Our logo is attached, we love the logo colours. Our website is www.velis4.com. We have high quality, chemical-free and organic ingredients and amazingly effective products. The packaging now needs to reflect the contents and the prices of the precious ingredients. We think we would like to stick to the amber glass, thinking of black lids. Want it to feel professional, classy, high-end, classic and not fussy. Would love for the packaging to feel fresh, beautiful, natural, expensive... yet still affordable luxury. New packaging could be predominantly grey and white with flash of the green. Our customer is busy and health conscious. She does not need a lot of fuss but loves using beautiful products. Some of our tag lines include - 'Beauty is being yourself but with a sparkle.' and 'Self-care is your divine responsibility.' Velis4 brightens every morning from within.' Can you please look at the product jars and bottles as well as the boxes that the oils will be packaged in.

Target Market(s)

30-50yr females, business women, entrepreneurs, health conscious mum's all with an awareness around the importance of chemical-free and organic products and a love for health, fitness and real beauty.

Colors

Requirements
Must have
• Our logo and our logo colours incorporated. As mentioned could be predominantly silver/grey and white with splash of green. The bottles could even be printed in the one silver/grey colour directly onto the glass as an option. Or labels to wrap around the bottles. Boxes (which are separate to the bottles) containing the products to be inviting and speak luxury. Must be recyclable in alignment with our values.
Nice to have
• Not sure whether to look at printing on the glass direct or complete wrap around labels (which will no doubt be cheaper to create). Would love a number of design options and ideas that give that beautiful feel and would make our customer so excited to want these products. Our packaging is over 8 years old and we have grown significantly in this time. It would be nice to have a new fresh look that reflects the quality and amazing efficacy of these products.
• One suggestion regarding the packaging for the essential oils is to categorise them - so the floral oils like lavender, geranium, neroli and rose all have a certain colour or something on the packaging to distinguish them as floral oils. Then we have herbal, spicy, woody, grass and citrus categories too. This could be shown on the box as opposed to the bottle.
• We also have four kinds of synergy blends that are based on the four main personality types eg: Powerful, Playful, Peaceful and Precise. No one necessarily knows this unless I am speaking but the oil blends that fit in here are Powerful - Harbor & Thistle, Copper Drift and Willow & Ember. Playful - Lantern & Tide, Pebble & Frost and Moss & Flint. Peaceful - Velvet Dune, Orchard & Hollow and Cloud & Cinder. Precise - Marble & Thread, Canyon & Reed and Quill & Meadow.
• I also love to incorporate the four seasons and we have four one-off seasonal blends called Sail Away (winter), Drift On (spring), Hum Low (summer) and Stay Put (autumn).
• If there was a strong element of natural beauty with this new packaging that would be amazing.
Should not have
• Lots of different wild out there colours. We love nature, and plants and order and clarity. Should not have too much information or busyness. Needs to be simple, elegant, classy, classic, beautiful. Please do not go cottage/lavender farm industry looking.

```html
<!DOCTYPE html>
<html lang="en">
<head>
<meta charset="utf-8">
<title>Velis4 Chamomile Roman Oil – Label Range</title>
<link rel="stylesheet" href="https://fonts.googleapis.com/css2?family=Jost:wght@300;400;500&family=Cormorant+Garamond:wght@400;500;600&display=swap">
<style>
  :root {
    --bg: #ecece8;
    --paper: #ffffff;
    --ink: #1a1a1a;
    --ink-soft: #3a3a3a;
    --leaf: #9ccc4a;
    --leaf-soft: #c5e08f;
    --placeholder: #e9ece4;
    --night: #0c0c0c;
    --night-dots: #262626;
    --gold: #b8862c;
    --rule: #8fa7bd;
    --caption: #555a60;
  }
  * { box-sizing: border-box; margin: 0; padding: 0; }
  html, body { width: 1200px; height: 849px; overflow: hidden; }
  body { background: var(--bg); font-family: "Jost", sans-serif; color: var(--ink); position: relative; }

  .label { position: absolute; top: 140px; height: 400px; overflow: hidden; }

  /* Label A – green band */
  .label--band { left: 80px; width: 320px; background: var(--paper); display: flex; }
  .band { width: 60px; background: var(--leaf); position: relative; flex: none; }
  .band__brand { position: absolute; left: 50%; top: 50%; transform: translate(-50%, -50%) rotate(-90deg);
    font-family: "Jost", sans-serif; font-weight: 400; font-size: 34px; letter-spacing: 0.12em; color: var(--ink); white-space: nowrap; }
  .band-body { flex: 1; padding: 22px 14px 0 14px; display: flex; flex-direction: column; }
  .band-body__title { font-weight: 500; font-size: 38px; line-height: 1.12; letter-spacing: 0.01em; }
  .band-body__line { font-weight: 300; font-size: 17px; padding: 4px 0; border-top: 1px solid var(--leaf-soft); color: var(--ink-soft); white-space: nowrap; }
  .band-body__line:first-of-type { margin-top: 10px; font-size: 20px; }
  .band-body__line:last-of-type { border-bottom: 1px solid var(--leaf-soft); }
  .band-body__photo { margin-top: 14px; flex: 1; background: var(--placeholder); }

  /* Label B – night */
  .label--night { left: 450px; width: 300px; background: var(--night); color: #f2f2f2; display: flex; }
  .dots { width: 28px; flex: none; background: var(--night-dots); }
  .night-body { flex: 1; text-align: center; font-family: "Cormorant Garamond", serif; padding-top: 40px; }
  .night-body__brand { font-size: 26px; font-weight: 500; letter-spacing: 0.16em; }
  .night-body__title { margin-top: 22px; font-size: 31px; line-height: 1.35; letter-spacing: 0.14em; }
  .night-body__code { display: block; margin: 16px auto 14px; width: 62px; height: 40px; border-radius: 50%; background: var(--gold); }
  .night-body__latin { font-size: 26px; }
  .night-body__spec { font-size: 23px; line-height: 1.0; margin-top: 8px; }
  .night-body__size { font-size: 18px; margin-top: 20px; }

  /* Label C – framed */
  .label--framed { left: 800px; width: 300px; background: var(--paper); text-align: center; padding-top: 48px; }
  .framed__brand { display: inline-flex; align-items: center; gap: 10px; font-size: 26px; letter-spacing: 0.14em; font-weight: 400; color: var(--ink-soft); }
  .framed__dot { width: 18px; height: 18px; border-radius: 50%; background: var(--leaf); }
  .framed__title { margin: 34px 22px 0; border: 3px solid var(--ink); padding: 8px 4px; font-weight: 300; font-size: 30px; line-height: 1.2; letter-spacing: 0.14em; }
  .framed__latin { margin-top: 22px; font-weight: 300; font-size: 25px; }
  .framed__spec { margin-top: 6px; font-weight: 300; font-size: 22px; line-height: 1.05; }
  .framed__size { margin-top: 16px; font-weight: 300; font-size: 18px; }

  /* Presentation */
  .pointer { position: absolute; left: 599px; top: 540px; width: 1px; height: 50px; background: var(--caption); }
  .caption { position: absolute; left: 0; right: 0; top: 596px; text-align: center; font-weight: 300; font-size: 32px; letter-spacing: 0.02em; color: var(--ink); }
  .footer-rule { position: absolute; left: 0; right: 0; top: 752px; height: 3px; background: var(--rule); }
  .footer-title { position: absolute; right: 12px; top: 782px; font-weight: 300; font-size: 13px; letter-spacing: 0.42em; color: var(--caption); }
</style>
</head>
<body>

  <section class="label label--band">
    <div class="band"><span class="band__brand">Velis4</span></div>
    <div class="band-body">
      <h2 class="band-body__title">CHAMOMILE<br>ROMAN OIL</h2>
      <p class="band-body__line">Arthemis nobilis</p>
      <p class="band-body__line">100% Pure Organic Essencial Oil</p>
      <p class="band-body__line">10ml/0.34 fl.oz ℮</p>
      <div class="band-body__photo" role="img" aria-label="Photograph of a chamomile flower with green leaves"></div>
    </div>
  </section>

  <section class="label label--night">
    <div class="dots" role="img" aria-label="Dotted pattern border"></div>
    <div class="night-body">
      <div class="night-body__brand">Velis4</div>
      <h2 class="night-body__title">CHAMOMILE<br>ROMAN OIL</h2>
      <span class="night-body__code" aria-label="Colour code: herbal"></span>
      <p class="night-body__latin">Arthemis nobilis</p>
      <p class="night-body__spec">100% pure<br>organic essencial oil</p>
      <p class="night-body__size">10ml/0.34 fl.oz ℮</p>
    </div>
    <div class="dots" role="img" aria-label="Dotted pattern border"></div>
  </section>

  <section class="label label--framed">
    <div class="framed__brand"><span class="framed__dot"></span>Velis4</div>
    <h2 class="framed__title">CHAMOMILE<br>ROMAN OIL</h2>
    <p class="framed__latin">Arthemis nobilis</p>
    <p class="framed__spec">100% pure<br>organic essencial oil</p>
    <p class="framed__size">10ml/0.34 fl.oz ℮</p>
  </section>

  <div class="pointer"></div>
  <p class="caption">COLOR CODIFICATION</p>

  <div class="footer-rule"></div>
  <p class="footer-title">PROPOSAL FOR VELIS4 PACKAGING</p>

</body>
</html>
```